Brochure Design Project

Our company is TEM Bexley Fold. (no LOGO)

We are a restaurant marketing and advertising service. We market restaurants menus by producing a menu guide, distributing flyers and post cards, and also placing the restaurants menu on our website for delivery.

We make restaurants more profitable, by making their food more accessible. Marketing restaurants on search engines, websites, friendloop, vrop, zindle, and a total of 21 different marketing techniques that make restaurants more money.

Key Point: This is all done at NO COST to the restaurant.

We are looking for a design for a brochure that will be mailed as well as handed to restaurateurs.

In my attached file I am including our sales letter. The letter can stay in letter form for the inside of a tri-fold brochure or it can be part of your design.

For more information about our service, please read the attached sales letter.

Target Market(s)

Restaurant Owners and General managers

Industry/Entity Type

Advertising

Requirements
Must have
• Must look attractive and Eye-catching

```html
<!DOCTYPE html>
<html lang="en">
<head>
<meta charset="utf-8">
<title>TEM Bexley Fold – Sales Flyer</title>
<link rel="stylesheet" href="https://fonts.googleapis.com/css2?family=Titan+One&family=Barlow:wght@300;400;600;700&display=swap">
<style>
  :root {
    --sky: #00a3e6;
    --navy: #2b3a66;
    --copy: #0aa0de;
    --footer-grey: #6e6e6e;
    --white: #ffffff;
    --ink-dark: #3a3540;
    --suit-light: #c9b3a8;
    --suit-dark: #9d8479;
  }
  * { margin: 0; padding: 0; box-sizing: border-box; }
  html, body { width: 800px; height: 1200px; overflow: hidden; background: var(--white); }
  .flyer {
    position: relative; width: 800px; height: 1200px; overflow: hidden;
    background: var(--white); font-family: "Barlow", sans-serif; color: var(--copy);
  }
  .top-bar { position: absolute; top: 0; left: 0; width: 800px; height: 45px; display: flex; }
  .top-bar .left { width: 400px; background: var(--sky); }
  .top-bar .right { flex: 1; background: var(--navy); }

  .headline {
    position: absolute; left: 74px; top: 111px; white-space: nowrap;
    font-family: "Titan One", sans-serif; font-weight: 400; font-size: 34.5px; line-height: 40px;
    letter-spacing: 0.5px; color: var(--navy); text-transform: uppercase;
    text-shadow: 2px 2px 0 var(--sky);
  }
  .subhead {
    position: absolute; left: 74px; top: 291px; color: var(--navy);
    font-weight: 300; text-transform: uppercase; white-space: nowrap;
  }
  .subhead .small { display: block; font-size: 32.5px; line-height: 36px; }
  .subhead .large { display: block; font-size: 41.5px; line-height: 44px; }

  .letter {
    position: absolute; left: 74px; top: 382px;
    font-size: 15.5px; line-height: 18.2px; font-weight: 400; white-space: nowrap;
  }
  .letter p { margin-bottom: 18.2px; }
  .letter .strong { font-weight: 700; }

  .portrait {
    position: absolute; left: 560px; top: 568px; width: 196px; height: 454px;
    border-radius: 70px 70px 16px 16px;
    background: linear-gradient(180deg, var(--ink-dark) 0%, var(--suit-light) 18%, var(--suit-dark) 100%);
    opacity: 0.85;
  }

  .footer-band { position: absolute; left: 0; top: 1039px; width: 800px; height: 19px; background: var(--navy); }
  .footer {
    position: absolute; left: 0; top: 1058px; width: 800px; height: 142px;
    background: var(--footer-grey); color: var(--white); padding: 20px 74px 0;
  }
  .footer .contact { font-weight: 700; font-size: 17.5px; line-height: 21px; }
  .footer .note { font-weight: 400; font-size: 13.5px; line-height: 18px; margin-top: 1px; }
</style>
</head>
<body>
<main class="flyer">
  <div class="top-bar"><div class="left"></div><div class="right"></div></div>

  <h1 class="headline">Would a check for $18,375<br>with your restaurants name<br>on it be worth<br>a 15 min conversation?</h1>

  <h2 class="subhead"><span class="small">Are you tired of ineffective</span><span class="large">marketing and advertising?</span></h2>

  <section class="letter">
    <p>If you answered yes to either question, we should talk about our all-inclusive<br>marketing plan. Our marketing plan places your menu in front of thousands of<br>customers each and every month. Hungry customers looking to buy immediately.<br>Hungry customers that want food now. The more views your menu receives,<br>the more likely a customer will purchase food from your restaurant.</p>
    <p>Ever have a problem with down time at your restaurant? Customers are not<br>dining in or taking out because it's too hot or too cold or it's raining outside?<br>That's a problem that you wouldn't have to have, if you made your food more<br>accessible.</p>
    <p>TEM Bexley Fold is a full service restaurant marketing and<br>advertising service that specializes in delivery.<br>We deliver food from a variety of restaurants to people at<br>their homes, offices, and hotels! Using our marketing<br>plan we will bring more exposure to your restaurant<br>and increase your bottom line.</p>
    <p class="strong">WE GUARANTEE IT!</p>
    <p>How many marketers and advertisers say that?<br>We do! We guarantee that you will only make money<br>and not pay money. There are never any participation<br>cost, or fees associated with our service.<br>We use a combination of 21 proven Marketing techniques<br>to drive your profits up while keeping cost down.</p>
    <p class="strong">So what should you do?<br>Call me now at 555-014-2290 to schedule a 15 min<br>consultation that is guaranteed to NOT cost you<br>anything and only make your restaurant money.</p>
    <p class="strong">Talk to you soon!</p>
  </section>

  <div class="portrait" role="img" aria-label="Photo of a smiling businesswoman in a taupe pantsuit standing with hands in pockets"></div>

  <div class="footer-band"></div>
  <footer class="footer">
    <div class="contact">Mara Quell<br>555-014-2290 (cell)<br>Bexleyfoldtem.com</div>
    <div class="note">I have a check with your restaurants name on it, so contact me before July 26, 2013!<br>You can also schedule an appointment online at bexleyfoldtem.com</div>
  </footer>
</main>
</body>
</html>
```